Business card design for counselling and psychotherapy practice

I am seeking a business card for a new venture into private practice. I am based in Brisbane Qld Australia. I provide holistic counselling and psychotherapy to individuals and groups.
Some words that describe the underpinnings of this practice would include: being, becoming, awareness, wholeness, contact, safety, acceptance, relationship, gestalt, paradox, interconnected, nature, process.
I would like to see designs that include earth colours.
The overall design should communicate safety and a curiosity of being and becoming.
Target Market(s)
this design is marketed toward women, professionals, lesbian, transgender, mothers
Industry/Entity Type
Safety
Contact Information for Business Card
Willow & Tide
Counselling and Psychotherapy
Maren Olcott
ph: 0417382905
email: maren.willow&tide@quietmail.net
www.willow&tidecounselling&psychotherapy.net
Logo styles of interest
Abstract Logo
Look and feel
Each slider illustrates characteristics of the customer's brand and the style your logo design should communicate.

```html
<!DOCTYPE html>
<html lang="en">
<head>
<meta charset="utf-8">
<title>Willow &amp; Tide — Business Cards</title>
<link rel="stylesheet" href="https://fonts.googleapis.com/css2?family=Questrial&display=swap">
<style>
  :root {
    --page-bg: #e9e6e1;
    --leaf-green: #6cc04a;
    --band-green: #74c452;
    --deep-green: #2f6e34;
    --mid-green: #4fae3c;
    --ink-grey: #4d4d4d;
    --soft-grey: #5e6a5a;
    --card-white: #ffffff;
  }
  * { margin: 0; padding: 0; box-sizing: border-box; }
  html, body {
    width: 1200px;
    height: 785px;
    overflow: hidden;
    background: var(--page-bg);
    font-family: "Questrial", "Century Gothic", sans-serif;
  }
  .canvas {
    position: relative;
    width: 1200px;
    height: 785px;
    display: flex;
    align-items: center;
    justify-content: center;
    gap: 40px;
  }
  .card {
    position: relative;
    width: 560px;
    height: 320px;
    overflow: hidden;
    box-shadow: 0 2px 6px rgba(0,0,0,0.12);
  }

  /* Front */
  .card--front { background: var(--leaf-green); }
  .card--front .brand {
    position: absolute;
    left: 200px;
    top: 108px;
  }
  .card--front .brand-mark {
    position: absolute;
    left: 58px;
    top: 70px;
    width: 120px;
    height: 120px;
    border-radius: 50%;
    background: rgba(255,255,255,0.85);
  }
  .card--front .brand-name { color: var(--card-white); }
  .card--front .brand-tagline { color: var(--soft-grey); }

  /* Back */
  .card--back { background: var(--card-white); }
  .card--back .band {
    position: absolute;
    left: 0; right: 0; bottom: 0;
    height: 48px;
    background: var(--band-green);
  }
  .card--back .brand-mark {
    position: absolute;
    left: 70px;
    top: 70px;
    width: 92px;
    height: 92px;
    border-radius: 50%;
    background: var(--mid-green);
  }
  .card--back .brand {
    position: absolute;
    left: 190px;
    top: 62px;
  }
  .card--back .brand-name { color: var(--deep-green); }
  .card--back .brand-tagline { color: var(--ink-grey); }

  .brand-name {
    font-size: 38px;
    line-height: 1;
    letter-spacing: 0.5px;
    white-space: nowrap;
  }
  .brand-tagline {
    margin-top: 4px;
    font-size: 23px;
    line-height: 1.1;
    white-space: nowrap;
  }

  .contact {
    position: absolute;
    right: 28px;
    top: 150px;
    text-align: right;
    color: var(--deep-green);
  }
  .contact-name {
    font-size: 19px;
    color: var(--mid-green);
    margin-bottom: 24px;
  }
  .contact-line {
    font-size: 18px;
    line-height: 1.3;
  }
</style>
</head>
<body>
  <main class="canvas">
    <section class="card card--front" aria-label="Card front">
      <span class="brand-mark" aria-hidden="true"></span>
      <div class="brand">
        <p class="brand-name">Willow &amp; Tide</p>
        <p class="brand-tagline">counselling and psychotherapy</p>
      </div>
    </section>

    <section class="card card--back" aria-label="Card back">
      <span class="brand-mark" aria-hidden="true"></span>
      <div class="brand">
        <p class="brand-name">Willow &amp; Tide</p>
        <p class="brand-tagline">counselling and psychotherapy</p>
      </div>
      <div class="contact">
        <p class="contact-name">Maren Olcott</p>
        <p class="contact-line">0417382905</p>
        <p class="contact-line">maren.willowandtide@quietmail.net</p>
      </div>
      <div class="band"></div>
    </section>
  </main>
</body>
</html>
```